" Minha empresa presta serviçoes de estética para gordura localizada, celulite, flacidez, rejuvenescimento, botox, preenchimento, redução de Estrias. Será uma marca licenciada para pessoas que queiram meus protocolos de atendimento. "

```html
<!DOCTYPE html>
<html lang="pt-BR">
<head>
<meta charset="utf-8">
<title>Mirela Duarte – Cartão de Visita</title>
<link href="https://fonts.googleapis.com/css2?family=Cinzel:wght@400;500&family=Montserrat:wght@400;500;600&display=swap" rel="stylesheet">
<style>
  :root{
    --bg:#e4e4e4;
    --black:#141414;
    --black-soft:#222;
    --white:#ffffff;
    --gold:#c49a4a;
    --gold-dark:#9a7430;
    --ink:#2a2a2a;
    --grey:#777;
  }
  *{margin:0;padding:0;box-sizing:border-box}
  html,body{width:1200px;height:1200px;overflow:hidden;background:var(--bg)}
  .canvas{position:relative;width:1200px;height:1200px}
  .card{position:absolute;left:210px;width:780px;height:450px;border-radius:30px;overflow:hidden;box-shadow:0 10px 30px rgba(0,0,0,.18)}
  .card--front{top:90px;background:linear-gradient(135deg,var(--black-soft),var(--black) 60%);border-bottom:10px solid var(--gold)}
  .card--back{top:640px;background:var(--white)}
  .brand{position:absolute;display:flex;flex-direction:column;align-items:center}
  .card--front .brand{left:0;right:0;top:125px}
  .brand__mark{width:74px;height:74px;border-radius:50%;background:linear-gradient(135deg,#e2c07a,var(--gold-dark));margin-bottom:22px}
  .brand__name{font-family:"Cinzel",serif;font-weight:400;letter-spacing:2px;color:var(--white);font-size:46px;line-height:1}
  .brand__tagline{font-family:"Montserrat",sans-serif;font-weight:500;color:var(--gold);font-size:17px;letter-spacing:7px;text-transform:uppercase;margin-top:10px}
  .card--back .brand{left:40px;top:140px;width:330px}
  .card--back .brand__mark{width:52px;height:52px;margin-bottom:14px}
  .card--back .brand__name{color:var(--ink);font-size:33px}
  .card--back .brand__tagline{font-size:12px;letter-spacing:5px;margin-top:8px}
  .contact{position:absolute;right:36px;top:40px;width:340px;font-family:"Montserrat",sans-serif;text-align:right}
  .contact__name{color:var(--gold);font-weight:600;font-size:19px;letter-spacing:1px}
  .contact__role{color:var(--grey);font-size:12px;letter-spacing:1px;margin-top:2px;margin-bottom:14px}
  .contact__list{list-style:none}
  .contact__item{display:flex;justify-content:flex-end;align-items:center;gap:12px;font-size:17px;color:var(--ink);height:44px}
  .icon{width:26px;height:26px;border-radius:5px;background:var(--gold);display:flex;align-items:center;justify-content:center;flex:none}
  .icon svg{width:16px;height:16px;fill:none;stroke:var(--white);stroke-width:2;stroke-linecap:round;stroke-linejoin:round}
  .contact__head{display:flex;justify-content:flex-end;align-items:center;gap:12px}
</style>
</head>
<body>
<main class="canvas">
  <section class="card card--front">
    <div class="brand">
      <span class="brand__mark"></span>
      <span class="brand__name">MIRELA DUARTE</span>
      <span class="brand__tagline">Estética Viva Bem</span>
    </div>
  </section>

  <section class="card card--back">
    <div class="brand">
      <span class="brand__mark"></span>
      <span class="brand__name">MIRELA DUARTE</span>
      <span class="brand__tagline">Estética Viva Bem</span>
    </div>
    <div class="contact">
      <div class="contact__head">
        <div>
          <div class="contact__name">NOME SOBRENOME</div>
          <div class="contact__role">CARGO/FUNÇÃO</div>
        </div>
        <span class="icon" style="margin-bottom:14px"><svg viewBox="0 0 16 16"><circle cx="8" cy="5" r="3"/><path d="M2 15c0-4 12-4 12 0"/></svg></span>
      </div>
      <ul class="contact__list">
        <li class="contact__item">nome@empresa.com.br<span class="icon"><svg viewBox="0 0 16 16"><rect x="1.5" y="3.5" width="13" height="9" rx="1"/><path d="M2 4l6 5 6-5"/></svg></span></li>
        <li class="contact__item">www.site.com.br<span class="icon"><svg viewBox="0 0 16 16"><circle cx="8" cy="8" r="6.5"/><path d="M1.5 8h13M8 1.5c3 3 3 10 0 13M8 1.5c-3 3-3 10 0 13"/></svg></span></li>
        <li class="contact__item">99 99999-9999<span class="icon"><svg viewBox="0 0 16 16"><rect x="4.5" y="1.5" width="7" height="13" rx="1.5"/><path d="M7 12.5h2"/></svg></span></li>
        <li class="contact__item">99 9999-9999<span class="icon"><svg viewBox="0 0 16 16"><path d="M3 2h3l1.5 3.5-2 1.5a8 8 0 0 0 3.5 3.5l1.5-2L14 10v3a1 1 0 0 1-1 1A11 11 0 0 1 2 3a1 1 0 0 1 1-1z"/></svg></span></li>
        <li class="contact__item">99 9999-9999<span class="icon"><svg viewBox="0 0 16 16"><rect x="2" y="3" width="12" height="10" rx="1.5"/><path d="M5 13v1.5M11 13v1.5"/></svg></span></li>
        <li class="contact__item">Rua do Projeto, 999<span class="icon"><svg viewBox="0 0 16 16"><path d="M8 15s5-5 5-9a5 5 0 0 0-10 0c0 4 5 9 5 9z"/><circle cx="8" cy="6" r="1.8"/></svg></span></li>
      </ul>
    </div>
  </section>
</main>
</body>
</html>
```